Site Re-Design For IT/Internet Services Site

Hi, We need a redevopment of our existing website (www.talvrek.com)
Pages That need designing are:
- Content Page (existing page: http://www.talvrek.com)
- Hotspot Locations Page (existing page: Http://www.talvrek.com/hotspot-locations/hotspot-locations.asp)
- Form page layout, including textbox, checkbox, radio buttons, drop down, submit/reset buttons, "required fields error message"
- Design of our subscription "plan selection" content page (https://secure.talvrek.com/?location=1001)
- Design of the NEXT TWO pages in the above subscription form, the "email/password page, to see this select less than 3 months, 1 hour, then continue and also the credit card page, see this by filling out left hand side "new account" form and continue Specs:
- The same navigation will be retained, but should be easily modifyable via PSD file.

- NOTE THAT FOR THE DESIGN COMPETITION, ONLY the CONTENT PAGE needs to be designed

- Existing Logo to Be Maintained and COMPLETELY UNCHANGE IN ANY ASPECT
- Similar format of dual navigation required. Currently main nav is horizontal with sub nav below, and "extra" nav available on left vertical strip. Does have to stay in this format, however main nav with subnav, and "extra" nav spots must be available
- Design should be fresh and innovative
- Colors are negotiable however typical design nono's will not be accepted (black content area etc) Code Requirements:
- PSD file should contain overall design, as well as sub PSD files for navigation to be easily re-created at a later date where required.

By negotiation after sucessful design chosen, extra design aspects such as: psd cutup in html, HTML markup compatible with IE6+, Chrome, Firefox required - Seperate CSS stylesheet - Images in sub folders as appropriate may be required.

Internet

5+ pages

• black background, etc.

```html
<!DOCTYPE html>
<html lang="en">
<head>
<meta charset="utf-8">
<title>Talvrek – Internet Kiosks – Features</title>
<link href="https://fonts.googleapis.com/css2?family=Arimo:wght@400;700&family=Questrial&display=swap" rel="stylesheet">
<style>
:root{
  --blue-deep:#0b4f94;
  --blue-mid:#1a79c4;
  --blue-light:#3d97d8;
  --blue-text:#0d5aa0;
  --lime:#b5cc2e;
  --lime-light:#d4e35e;
  --lime-dark:#8aa21c;
  --panel-white:#f6f8fa;
  --text:#333;
  --text-soft:#555;
  --menu-dark:#2a2a2a;
}
*{margin:0;padding:0;box-sizing:border-box}
html,body{width:1200px;height:840px;overflow:hidden;background:#fff}
body{position:relative;font-family:"Arimo",Arial,sans-serif;color:var(--text)}
.abs{position:absolute}
.header-band{left:0;top:0;width:1200px;height:169px;background:linear-gradient(180deg,var(--blue-mid) 0%,var(--blue-light) 55%,var(--blue-deep) 100%)}
.nav-band{left:0;top:169px;width:1200px;height:34px;background:linear-gradient(180deg,var(--lime-dark) 0%,var(--lime) 20%,var(--lime) 80%,var(--lime-light) 100%)}
.logo-box{left:233px;top:15px;width:148px;height:139px;background:var(--panel-white);border:4px solid var(--lime);display:flex;align-items:center;justify-content:center;gap:6px}
.logo-box .mark{width:12px;height:12px;background:var(--blue-deep)}
.logo-box .name{font-family:"Questrial",sans-serif;font-size:20px;color:var(--blue-deep)}
.badge{background:var(--panel-white);border:4px solid var(--lime);display:flex;align-items:center;justify-content:center}
.badge span{display:block;width:36px;height:36px;border-radius:50%;background:#c8c8c8}
.badge .sq{border-radius:6px;width:40px;height:26px}
.search-panel{left:463px;top:16px;width:496px;height:138px;background:linear-gradient(135deg,#2f84cc,#5aa6e2 60%,#2d80c6);border-radius:4px;overflow:hidden}
.search-brand{left:187px;top:14px;width:64px;height:24px;background:#fff;border-radius:5px;font-size:13px;color:var(--blue-deep);display:flex;align-items:center;justify-content:center}
.search-input{left:256px;top:17px;width:167px;height:18px;background:#fff;border:1px solid #9cc}
.search-btn{left:428px;top:17px;width:48px;height:18px;background:var(--lime);border-radius:9px;font-size:8px;color:#234;display:flex;align-items:center;justify-content:center}
.search-opts{left:258px;top:42px;font-size:8px;color:#fff;display:flex;gap:14px}
.search-opts i{display:inline-block;width:8px;height:8px;border-radius:50%;background:#fff;margin-right:5px;vertical-align:-1px}
.util-bar{left:76px;top:106px;width:420px;height:32px;background:rgba(20,80,150,.35);display:flex;font-family:"Questrial",sans-serif;font-size:11px;color:#fff}
.util-bar div{flex:1;display:flex;align-items:center;justify-content:center;gap:6px;border-right:1px solid rgba(255,255,255,.25)}
.util-bar div:last-child{border:none}
.util-bar b{display:inline-block;width:13px;height:13px;border-radius:50%;background:#8ac4f0}
.main-nav{left:233px;top:173px;width:722px;height:27px;display:flex;font-family:"Questrial",sans-serif;font-size:11.5px;color:#111}
.main-nav a{display:flex;align-items:center;justify-content:center;border-left:1px solid rgba(255,255,255,.5);text-decoration:none;color:inherit}
.main-nav a:last-child{border-right:1px solid rgba(255,255,255,.5)}
.breadcrumb{left:235px;top:216px;font-size:9.5px;font-weight:700;color:#666}
.side-menu{left:233px;top:240px;width:176px}
.side-menu a{display:flex;align-items:center;height:23px;margin-bottom:9px;border:2px solid var(--lime);border-radius:3px;background:linear-gradient(#555,#3a3a3a);color:var(--lime);font-size:10.5px;font-weight:700;text-decoration:none;padding-left:8px}
.side-menu a.active{background:linear-gradient(#333,#111)}
.side-menu a::before{content:"";border-left:5px solid var(--lime);border-top:4px solid transparent;border-bottom:4px solid transparent;margin-right:8px}
.promo{left:233px;top:375px;width:175px;height:81px;border:2px solid #ccc;border-radius:4px;background:linear-gradient(#fafafa,#e4e8ec);font-family:"Questrial",sans-serif;text-align:right;padding:5px 10px 0 0;line-height:1}
.promo .l1{font-size:20px;color:#888}.promo .l1 b{color:#4b93cf}
.promo .l2{font-size:16px;color:#999}.promo .l2 b{color:#4b93cf}
.promo .l3{font-size:24px;color:#777}.promo .l3 b{color:#2a7fc4}
.promo .signal{left:8px;top:8px;width:46px;height:62px;border-radius:50%;background:radial-gradient(#9cc9ea,#cfe3f2 70%,transparent 72%)}
.page-title{left:423px;top:228px;font-family:"Questrial",sans-serif;font-size:25px;color:var(--blue-text)}
.photo{left:425px;top:277px;width:222px;height:143px;border:2px solid #ccc;border-radius:4px;background:linear-gradient(#f2f2f2 0%,#e6e6e6 55%,#8a8fa0 72%,#5a5575 100%)}
.intro{left:659px;top:273px;width:296px;font-size:13.3px;line-height:16.5px;text-align:justify;color:#222}
.intro a{color:var(--lime-dark);text-decoration:underline}
.body-copy{left:422px;top:437px;width:533px;font-size:9.4px;line-height:16.5px;text-align:justify;color:var(--text-soft)}
.body-copy p{margin-bottom:16.5px}
.footer{left:233px;top:667px;width:722px;height:85px;border:2px solid var(--lime-dark);border-radius:4px;background:linear-gradient(var(--lime-light),var(--lime) 40%,var(--lime-dark))}
.footer .site{left:18px;top:10px;font-size:26px;font-weight:700;color:var(--blue-text)}
.footer .rule{left:18px;top:48px;width:232px;height:1px;background:rgba(255,255,255,.6)}
.footer .tel{left:22px;top:56px;font-size:13px;font-weight:700;color:rgba(255,255,255,.75)}
.footer .divider{left:274px;top:6px;width:2px;height:71px;background:#6e8416}
.footer-links{left:292px;top:11px;display:grid;grid-template-columns:140px 149px 110px;row-gap:9.5px;font-family:"Questrial",sans-serif;font-size:9px;color:#4a5a10}
.footer-links span::before{content:"→ ";color:var(--blue-text)}
.copyright{left:700px;top:760px;width:255px;text-align:right;font-size:8px;color:var(--blue-mid)}
</style>
</head>
<body>
<div class="abs header-band"></div>
<div class="abs nav-band"></div>

<div class="abs logo-box"><span class="mark"></span><span class="name">talvrek</span></div>
<div class="abs badge" style="left:389px;top:16px;width:65px;height:64px"><span></span></div>
<div class="abs badge" style="left:389px;top:89px;width:65px;height:64px"><span></span></div>
<div class="abs badge" style="left:462px;top:89px;width:65px;height:64px"><span class="sq"></span></div>

<div class="abs search-panel">
  <div class="abs search-brand">Findly</div>
  <div class="abs search-input"></div>
  <div class="abs search-btn">SEARCH</div>
  <div class="abs search-opts"><span><i></i>Web</span><span><i></i>www.talvrek.com</span><span><i></i>secure.talvrek.com</span></div>
  <div class="abs util-bar"><div><b></b>FAQ'S</div><div><b></b>CONTACT US</div><div><b></b>MY ACCOUNT</div></div>
</div>

<nav class="abs main-nav">
  <a style="width:95px">HOME</a><a style="width:172px">WIRELESS HOTSPOTS</a><a style="width:150px">INTERNET KIOSKS</a><a style="width:183px">HOTSPOT LOCATIONS</a><a style="width:122px">RESELLERS</a>
</nav>

<div class="abs breadcrumb">Home &nbsp;-&nbsp; Internet Kiosks</div>

<nav class="abs side-menu">
  <a class="active">Features</a><a>Benefits</a><a>Kiosk types</a><a>Prices</a>
</nav>

<div class="abs promo">
  <div class="abs signal"></div>
  <div class="l1"><b>We</b> have</div>
  <div class="l2">the <b>solution</b></div>
  <div class="l3">for <b>you</b></div>
</div>

<h1 class="abs page-title">Features</h1>
<div class="abs photo" role="img" aria-label="Photo of three business people seated at a boardroom table"></div>
<p class="abs intro">Talvrek Wireless Solutions was founded to address the emerging and rapidly growing public demand for wireless internet access. A wireless hotspot service provision pioneer, we enable hotels, clubs, airports, motels, schools and universities, accommodation providers and cafes to offer a value added service that generates an additional revenue stream. Further information on our wireless hotspot system can be <a>found here</a>.</p>

<div class="abs body-copy">
  <p>Although a staggering 80% of the Australian population are now online, many are still tethered to their desks when accessing the internet. Talvrek's vision is to create a world of ubiquitous wireless internet access, without sacrificing the rich experience you get from your office, school, or home. In today's fast-moving world, people are used to being able to access the services they want, whenever and wherever they want them. Mobile professionals, everyday laptop-toting businessmen and students - they all need access to the internet at the push of a button, on the go.</p>
  <p>Wi-Fi is set to dramatically change the landscape of work and communication, more so than any technology since the advent of the internet. The progressive growth of Wi-Fi and its adoption across both large and small businesses, as well as through different vertical industries, means that it will soon become mainstream. All around the globe, publicly accessible wireless internet hotspots are springing up in airports, hotels, coffee shops, and restaurants. Those businesses slow on the uptake risk being left behind.</p>
</div>

<footer class="abs footer">
  <div class="abs site">www.talvrek.com</div>
  <div class="abs rule"></div>
  <div class="abs tel">T: 1800 555 014 &nbsp; F: (07) 5550 0142</div>
  <div class="abs divider"></div>
  <div class="abs footer-links">
    <span>HOME</span><span>HOTSPOT LOCATIONS</span><span>CONTACT US</span>
    <span>WIRELESS HOTSPOTS</span><span>RESELLERS</span><span>MY ACCOUNT</span>
    <span>INTERNET KIOSKS</span><span>FAQ'S</span><span></span>
  </div>
</footer>
<div class="abs copyright">All Content Copyright Talvrek Pty Ltd 2006</div>
</body>
</html>
```